German Headhunter/ HR Consultancy needs Business Cards Design

We need a business Card Design for our Company in Stuttgart. We are specialized as Headhunter/ HR Consultancy in Placement of specialist and managers in permanent employment. Please refer to our business logo.

```html
<!DOCTYPE html>
<html lang="de">
<head>
<meta charset="utf-8">
<title>Kerntal Personalberatung – Visitenkarte</title>
<link rel="stylesheet" href="https://fonts.googleapis.com/css2?family=Montserrat:wght@500;600;700&family=Arimo:wght@400&display=swap">
<style>
  :root {
    --page-bg: #e8e7e5;
    --card-white: #ffffff;
    --brand-blue: #3b4fb3;
    --brand-blue-dark: #2e3f98;
    --brand-blue-light: #5366c4;
    --text-grey: #8c8c8c;
    --rule-grey: #b5b5b5;
  }
  * { box-sizing: border-box; margin: 0; padding: 0; }
  html, body { width: 1200px; height: 802px; overflow: hidden; }
  body {
    background: var(--page-bg);
    display: flex;
    align-items: center;
    justify-content: center;
    gap: 60px;
    font-family: "Arimo", Arial, sans-serif;
  }
  .card {
    width: 525px;
    height: 300px;
    position: relative;
    box-shadow: 0 6px 18px rgba(0,0,0,0.12);
  }

  /* Front side */
  .card--front { background: var(--card-white); }
  .brand {
    position: absolute;
    top: 58px;
    left: 0; right: 0;
    display: flex;
    align-items: center;
    justify-content: center;
    gap: 14px;
  }
  .brand__mark {
    width: 26px; height: 26px;
    background: var(--brand-blue);
  }
  .brand__name {
    font-family: "Montserrat", sans-serif;
    font-weight: 700;
    color: var(--brand-blue);
    font-size: 25px;
    letter-spacing: 0.5px;
    line-height: 1.05;
  }
  .brand__name span { display: block; font-size: 11.5px; letter-spacing: 1.2px; }
  .details {
    position: absolute;
    top: 140px;
    left: 0; right: 0;
    display: flex;
    justify-content: center;
    align-items: center;
    gap: 22px;
  }
  .person { text-align: right; }
  .person__name {
    font-family: "Montserrat", sans-serif;
    font-weight: 600;
    color: var(--brand-blue);
    font-size: 17px;
    letter-spacing: 0.5px;
  }
  .person__role { color: var(--text-grey); font-size: 13px; margin-top: 2px; }
  .divider { width: 1px; height: 64px; background: var(--rule-grey); }
  .contact { list-style: none; color: var(--text-grey); font-size: 12.5px; }
  .contact li { display: flex; align-items: center; gap: 8px; line-height: 21px; }
  .contact svg { width: 12px; height: 12px; fill: var(--brand-blue); }
  .address {
    position: absolute;
    bottom: 36px; left: 0; right: 0;
    text-align: center;
    color: var(--text-grey);
    font-size: 12.5px;
  }

  /* Back side */
  .card--back { overflow: hidden; }
  .back__pattern {
    position: absolute; inset: 0;
    background: linear-gradient(135deg, var(--brand-blue-light) 0%, var(--brand-blue) 45%, var(--brand-blue-dark) 100%);
  }
  .back__brand {
    position: absolute;
    right: 48px; top: 50%;
    transform: translateY(-50%);
    display: flex; align-items: center; gap: 14px;
  }
  .back__brand .brand__mark { background: #ffffff; width: 30px; height: 30px; }
  .back__brand .brand__name { color: #ffffff; font-size: 22px; }
  .back__brand .brand__name span { font-size: 10px; }
</style>
</head>
<body>
  <section class="card card--front">
    <div class="brand">
      <div class="brand__mark"></div>
      <div class="brand__name">KERNTAL<span>PERSONALBERATUNG</span></div>
    </div>
    <div class="details">
      <div class="person">
        <div class="person__name">JONATHAN SMITH</div>
        <div class="person__role">Manager</div>
      </div>
      <div class="divider"></div>
      <ul class="contact">
        <li><svg viewBox="0 0 24 24"><path d="M6.6 10.8a15.1 15.1 0 0 0 6.6 6.6l2.2-2.2a1 1 0 0 1 1-.25 11.4 11.4 0 0 0 3.6.57 1 1 0 0 1 1 1V20a1 1 0 0 1-1 1A17 17 0 0 1 3 4a1 1 0 0 1 1-1h3.5a1 1 0 0 1 1 1c0 1.25.2 2.45.57 3.57a1 1 0 0 1-.25 1z"/></svg>123-456-2100</li>
        <li><svg viewBox="0 0 24 24"><path d="M2 5h20v14H2z M2 5l10 8 10-8" /></svg>hello@kerntal-mail.de</li>
        <li><svg viewBox="0 0 24 24"><circle cx="12" cy="12" r="10"/></svg>www.kerntal-hr.de</li>
      </ul>
    </div>
    <p class="address">Your address, city, state, ZIP 0000</p>
  </section>

  <section class="card card--back">
    <div class="back__pattern" role="img" aria-label="Embossed repeating brand pattern in blue tones"></div>
    <div class="back__brand">
      <div class="brand__mark"></div>
      <div class="brand__name">KERNTAL<span>PERSONALBERATUNG</span></div>
    </div>
  </section>
</body>
</html>
```